Simple Business Cards for Self-employed Coach

Simple business card with a design that includes the QLT logo.
Using either only the logo color or additional colors that match the logo.

Meridian Guides reach deeply into the past, gathering wisdom from East and West, while still staying current with the frontiers of new discovery in cognitive science, genetics, and other disciplines. see https://www.brightharborpath.example/what-is-integral-coaching/

Target Market(s)

Coaching Clients in Tokyo /Asia; in business organizations, but also outside

Industry/Entity Type

Life Coaching

Contact Information for Business Card

Lukas Brenning
Certified Meridian Guide

3-2-48 Kamiyoshi
Nakarino 164-0392
Tokyo, Japan

Phone: +81 70 4817 5062
E-Mail: lukas.brenning@mailora.example

Font styles to use
Sans Serif

Colors
00a990

Requirements
Must have
• include uploaded logo
• color fitting with QLT logo color
Nice to have
• simple, elegant design
Should not have
• clutter

```html
<!DOCTYPE html>
<html lang="en">
<head>
<meta charset="utf-8">
<title>QLT Business Card</title>
<link rel="stylesheet" href="https://fonts.googleapis.com/css2?family=Roboto:wght@400;500;700&display=swap">
<style>
  :root {
    --teal: #00a990;
    --teal-dark: #008c78;
    --teal-light: #12b8a0;
    --card-white: #f7f7f7;
    --card-shade: #e6e6e6;
    --ink: #1f2a2a;
    --page: #d9d9d6;
    --white: #ffffff;
  }
  * { margin: 0; padding: 0; box-sizing: border-box; }
  html, body {
    width: 1200px; height: 1023px; overflow: hidden;
    background: var(--page);
    font-family: "Roboto", sans-serif;
  }
  .stage {
    width: 1200px; height: 1023px;
    display: flex; align-items: center; justify-content: center;
  }
  .card {
    position: relative;
    width: 1050px; height: 600px;
    border-radius: 28px;
    background: linear-gradient(135deg, var(--white) 0%, var(--card-white) 55%, var(--card-shade) 100%);
    box-shadow: 0 14px 36px rgba(0,0,0,0.18);
    overflow: hidden;
  }
  .brand {
    position: absolute; left: 64px; top: 64px;
    display: flex; align-items: center; gap: 16px;
  }
  .brand-square {
    width: 38px; height: 38px; background: var(--teal);
  }
  .brand-name {
    font-weight: 700; font-size: 54px; letter-spacing: 10px;
    color: var(--teal);
  }
  .band {
    position: absolute; left: 0; right: 0; top: 318px; height: 200px;
    background: linear-gradient(90deg, var(--teal-light) 0%, var(--teal) 45%, var(--teal-dark) 100%);
    display: flex;
  }
  .identity {
    width: 560px; padding: 0 0 0 64px;
    display: flex; flex-direction: column; justify-content: flex-end;
    padding-bottom: 26px;
  }
  .person-name {
    font-weight: 700; font-size: 44px; color: var(--white);
  }
  .person-title {
    font-weight: 500; font-size: 26px; color: var(--ink); margin-top: 4px;
  }
  .divider {
    width: 2px; background: rgba(255,255,255,0.75);
  }
  .contact {
    padding: 22px 0 0 34px;
    color: var(--white); font-size: 21px; letter-spacing: 1px; line-height: 29px;
    list-style: none;
  }
  .contact li { display: flex; align-items: center; gap: 12px; }
  .contact .address-line { padding-left: 0; }
  .contact svg { width: 20px; height: 20px; flex: none; }
</style>
</head>
<body>
<main class="stage">
  <section class="card">
    <div class="brand">
      <span class="brand-square"></span>
      <span class="brand-name">QLT</span>
    </div>
    <div class="band">
      <div class="identity">
        <p class="person-name">Lukas Brenning</p>
        <p class="person-title">Certified Meridian Guide</p>
      </div>
      <div class="divider"></div>
      <ul class="contact">
        <li class="address-line">3-2-48 Kamiyoshi</li>
        <li class="address-line">Nakarino 164-0392 Tokyo, Japan</li>
        <li>
          <svg viewBox="0 0 20 20"><circle cx="10" cy="10" r="8.5" fill="none" stroke="#fff" stroke-width="1.6"/><path d="M7 6.5c.6-.5 1.3-.3 1.6.4l.5 1.1c.2.5 0 .9-.4 1.2.5 1 1.2 1.7 2.1 2.2.3-.4.8-.6 1.3-.4l1.1.5c.6.3.8 1 .3 1.6-.9 1-2.5.8-4.2-.6-1.8-1.6-3-3.6-2.3-6z" fill="#fff"/></svg>
          +81 70 4817 5062
        </li>
        <li>
          <svg viewBox="0 0 20 20"><rect x="2" y="4.5" width="16" height="11" fill="none" stroke="#fff" stroke-width="1.6"/><path d="M2 4.5l8 6.5 8-6.5M2 15.5l6-5M18 15.5l-6-5" fill="none" stroke="#fff" stroke-width="1.4"/></svg>
          lukas.brenning@mailora.example
        </li>
        <li>
          <svg viewBox="0 0 20 20"><circle cx="10" cy="10" r="8" fill="none" stroke="#fff" stroke-width="1.6"/><ellipse cx="10" cy="10" rx="3.5" ry="8" fill="none" stroke="#fff" stroke-width="1.3"/><path d="M2 10h16M3.5 6h13M3.5 14h13" stroke="#fff" stroke-width="1.2"/></svg>
          www.brightharborpath.example
        </li>
      </ul>
    </div>
  </section>
</main>
</body>
</html>
```